Wiz4Giggle website

We need a website called Wiz 4 Giggle (wiz4giggle.example).
This site is for fun (just like 7lol.example, flopdiary.example, jokepapa.example etc. You know what I mean, right?)
so we are open to different designs/looks. We are looking for a simple and clean and fun design to make it easy to use for our users.

The design of Wiz4Giggle should be different from other fun site (better than others, I mean), and this is what we want you to do.

The style for our site should be in (or be similar to, at least) the BLOG way, (If you can't catch my words, have a look at 7LOL or Flopdiary).

But at meantime, I'd like to stress again that we want this site be different from the sites like 7LOL and FlopDiary.
Updates

i have a logo for the website now.

http://media.artmarket.example/works/31904_265017_80391_preview.jpg

pls try to fit this logo into the website design.

Requirements
Must have
• We need at least following pages designed:

1. front page (index.jpg)

2. login form page (login.jpg)

3. registeration form page (register.jpg)

4. content page (post.jpg)

5. submit photo form page (submit.jpg)

6. user profile page (user_center.jpg)

```html
<!DOCTYPE html>
<html lang="en">
<head>
<meta charset="utf-8">
<title>Wiz4Giggle</title>
<link rel="stylesheet" href="https://fonts.googleapis.com/css2?family=Arimo:wght@400;700&display=swap">
<style>
:root{
  --brown:#4a2c05;
  --brown-dark:#3a2204;
  --orange:#f9a100;
  --orange-deep:#e88c00;
  --cream:#fdf2e0;
  --white:#ffffff;
  --text:#3b2a12;
  --muted:#7a6a58;
  --line:#e3d7c4;
  --blue:#2a8fc7;
  --sky:#7fd3ee;
  --navy:#3b5a9a;
  --like:#f0a35a;
}
*{margin:0;padding:0;box-sizing:border-box}
html,body{width:1200px;height:986px;overflow:hidden;background:var(--cream);font-family:"Arimo",Arial,sans-serif;color:var(--text)}
.page{position:relative;width:1200px;height:986px}
.abs{position:absolute}

/* header */
.header{left:0;top:0;width:1200px;height:141px;background:var(--brown)}
.header-top{left:0;top:0;width:1200px;height:12px;background:var(--orange)}
.account-tab{left:814px;top:0;width:386px;height:52px;background:var(--orange);border-bottom-left-radius:46px 52px}
.header-band{left:0;top:141px;width:1200px;height:45px;background:linear-gradient(var(--orange),var(--orange-deep))}
.logo{left:18px;top:44px;font-weight:700;font-size:50px;color:#d9a24a;letter-spacing:-1px}
.btn{top:12px;height:31px;border-radius:4px;background:var(--brown-dark);color:var(--white);font-size:16px;line-height:31px;text-align:center;border:1px solid #1f1202}
.btn-login{left:857px;width:66px}
.btn-register{left:935px;width:89px}
.social{top:12px;width:29px;height:29px;border-radius:4px}
.social-a{left:1042px;background:var(--sky)}
.social-b{left:1078px;background:#1b7bb0}
.social-c{left:1113px;background:var(--navy)}

.nav-item{width:130px;height:130px}
.nav-art{left:30px;top:0;width:70px;height:90px;border-radius:40px 40px 20px 20px;background:radial-gradient(circle at 50% 60%,#ffffff,#e3dde5 70%,#c9b9c6)}
.nav-sign{left:7px;height:30px;width:116px;border-radius:4px;background:linear-gradient(#b8842f,#8c5f1e);color:var(--white);font-weight:700;font-size:20px;text-align:center;line-height:30px;box-shadow:0 2px 0 #5a3a10}
.nav-shadow{left:0;width:130px;height:18px;border-radius:50%;background:rgba(90,50,0,.35)}

/* body */
.main{left:0;top:186px;width:1200px;height:745px;background:var(--cream);border:1px solid #d9c9a8}
.panel{background:var(--white);border-radius:5px;box-shadow:0 0 5px rgba(0,0,0,.25);overflow:hidden}
.panel-title{height:49px;background:var(--brown);color:var(--white);font-size:22px;line-height:49px;padding-left:19px}
.thumb{border:1px solid #b8b0a6;box-shadow:0 0 2px rgba(0,0,0,.2)}
.t-elephant{background:linear-gradient(160deg,#8c9a78,#6d6656 55%,#c9c4b8)}
.t-cart{background:linear-gradient(170deg,#c8c0b0,#e6ddca 40%,#8a7d62)}
.t-kitten{background:linear-gradient(170deg,#e2dde2,#d8c8b8 60%,#b88450)}
.t-hamster{background:linear-gradient(160deg,#c9202a,#d6d0c8 55%,#a51820)}
.t-chick{background:linear-gradient(150deg,#6f7a3a,#b8ad94 40%,#8a8480 70%,#3e4a22)}
.play{left:50%;top:50%;width:58px;height:58px;margin:-29px 0 0 -29px}
.item-title{font-size:22px;color:#1d1408}
.stats{display:flex;align-items:center;gap:6px;font-size:14px;color:var(--muted)}
.stats svg{display:block}
.divider{height:2px;background:var(--line)}

/* posts */
.post-heading{font-size:29px;color:#3b2706;font-weight:400}
.post-frame{width:315px;height:283px;background:#e2e0de;border:1px solid #cfcac4;border-radius:3px}
.post-image{left:20px;top:17px;width:275px;height:249px;border:2px solid #9c9690}
.post-name{font-size:22px;font-weight:700;color:#3b2706}
.post-text{width:240px;font-size:13.4px;line-height:22px;color:var(--muted)}
.post-meta{font-size:14px;color:var(--muted)}
.post-meta b{font-size:16px;color:#2a1d0c;margin-right:6px}
.share-box{width:235px;height:134px;background:linear-gradient(#fff,#ececec);border:1px solid #d6d2cc;border-radius:4px}
.share-btn{left:13px;width:92px;height:31px;border-radius:3px;color:var(--white);font-size:11px;font-weight:700;line-height:31px;padding-left:32px}
.share-btn i{position:absolute;left:4px;top:5px;width:21px;height:21px;border-radius:3px;background:rgba(255,255,255,.35)}
.share-a{background:var(--sky)}
.share-b{background:var(--navy)}
.count{left:112px;width:46px;height:31px;border:1px solid #9ab;border-radius:3px;background:var(--white);font-size:17px;line-height:29px;text-align:center;color:#333}
.count::before{content:"";position:absolute;left:-6px;top:10px;width:9px;height:9px;background:var(--white);border-left:1px solid #9ab;border-bottom:1px solid #9ab;transform:rotate(45deg)}
.like-btn{left:164px;width:60px;height:31px;border:1px solid #b6c4dc;border-radius:3px;background:#eef2f9;font-size:13px;line-height:29px;color:#3a6aa8;padding-left:30px}
.like-btn i{position:absolute;left:3px;top:4px;width:22px;height:22px;border-radius:3px}
.post-rule{left:245px;width:569px;height:2px;background:linear-gradient(90deg,transparent,#e6c98a,transparent)}

/* footer */
.footer{left:0;top:934px;width:1200px;height:52px;background:var(--orange);border-top:2px solid var(--orange-deep);text-align:center;font-size:15px;line-height:50px;color:#2a1a05}
</style>
</head>
<body>
<div class="page">

<svg width="0" height="0" style="position:absolute">
  <defs>
    <symbol id="icon-comment" viewBox="0 0 24 24"><rect x="1" y="2" width="22" height="15" rx="2" fill="#2a8fc7"/><path d="M7 17l0 6 6-6z" fill="#2a8fc7"/><path d="M5 7h14M5 11h10" stroke="#fff" stroke-width="1.6"/></symbol>
    <symbol id="icon-like" viewBox="0 0 24 24"><path d="M2 10h5v12H2z" fill="#3b6fb6"/><path d="M8 10l5-8c2 0 3 1 2.5 3L14 9h7c1.5 0 2 1.5 1.5 2.5L20 21H8z" fill="#f0a35a"/></symbol>
    <symbol id="icon-play" viewBox="0 0 58 58"><circle cx="29" cy="29" r="27" fill="rgba(90,90,90,.75)" stroke="#fff" stroke-width="3"/><path d="M22 16l20 13-20 13z" fill="#fff"/></symbol>
  </defs>
</svg>

<header>
  <div class="abs header"></div>
  <div class="abs header-top"></div>
  <div class="abs account-tab"></div>
  <div class="abs header-band"></div>
  <div class="abs logo">Wiz4Giggle</div>
  <div class="abs btn btn-login">Login</div>
  <div class="abs btn btn-register">Register</div>
  <div class="abs social social-a"></div>
  <div class="abs social social-b"></div>
  <div class="abs social social-c"></div>

  <nav>
    <div class="abs nav-item" style="left:345px;top:46px">
      <div class="abs nav-art" role="img" aria-label="Mascot illustration above the Home link"></div>
      <div class="abs nav-sign" style="top:62px">Home</div>
      <div class="abs nav-shadow" style="top:102px"></div>
    </div>
    <div class="abs nav-item" style="left:482px;top:72px">
      <div class="abs nav-art" role="img" aria-label="Mascot illustration above the About link"></div>
      <div class="abs nav-sign" style="top:57px">About</div>
      <div class="abs nav-shadow" style="top:90px"></div>
    </div>
    <div class="abs nav-item" style="left:621px;top:72px">
      <div class="abs nav-art" role="img" aria-label="Mascot illustration above the Vote link"></div>
      <div class="abs nav-sign" style="top:57px">Vote</div>
      <div class="abs nav-shadow" style="top:90px"></div>
    </div>
    <div class="abs nav-item" style="left:758px;top:72px">
      <div class="abs nav-art" role="img" aria-label="Mascot illustration above the Hot link"></div>
      <div class="abs nav-sign" style="top:57px">Hot</div>
      <div class="abs nav-shadow" style="top:90px"></div>
    </div>
    <div class="abs nav-item" style="left:896px;top:72px">
      <div class="abs nav-art" role="img" aria-label="Mascot illustration above the Fun link"></div>
      <div class="abs nav-sign" style="top:57px">Fun</div>
      <div class="abs nav-shadow" style="top:90px"></div>
    </div>
  </nav>
</header>

<main>
  <div class="abs main"></div>

  <aside class="abs panel" style="left:18px;top:204px;width:208px;height:718px">
    <div class="panel-title">Populer Video</div>
    <div class="abs thumb t-elephant" style="left:20px;top:69px;width:169px;height:131px" role="img" aria-label="Video still of an elephant beside a toilet"><svg class="abs play"><use href="#icon-play"/></svg></div>
    <div class="abs item-title" style="left:19px;top:211px">Lorem Ipsum</div>
    <div class="abs stats" style="left:19px;top:243px"><svg width="26" height="26"><use href="#icon-comment"/></svg>101<svg width="26" height="26"><use href="#icon-like"/></svg>200</div>
    <div class="abs divider" style="left:0;top:286px;width:208px"></div>

    <div class="abs thumb t-cart" style="left:20px;top:299px;width:169px;height:131px" role="img" aria-label="Video still of a bicycle piled with boxes"><svg class="abs play"><use href="#icon-play"/></svg></div>
    <div class="abs item-title" style="left:19px;top:441px">Lorem Ipsum</div>
    <div class="abs stats" style="left:19px;top:475px"><svg width="26" height="26"><use href="#icon-comment"/></svg>101<svg width="26" height="26"><use href="#icon-like"/></svg>200</div>
    <div class="abs divider" style="left:0;top:516px;width:208px"></div>

    <div class="abs thumb t-kitten" style="left:20px;top:529px;width:169px;height:131px" role="img" aria-label="Video still of a kitten standing with raised paws"><svg class="abs play"><use href="#icon-play"/></svg></div>
    <div class="abs stats" style="left:19px;top:677px"><svg width="26" height="26"><use href="#icon-comment"/></svg>101<svg width="26" height="26"><use href="#icon-like"/></svg>200</div>
  </aside>

  <article>
    <h2 class="abs post-heading" style="left:244px;top:205px">Lorem Ipsum is simply dummy</h2>
    <div class="abs post-frame" style="left:245px;top:253px"><div class="abs post-image t-chick" role="img" aria-label="Photo of a yellow chick beside a grey kitten"></div></div>
    <div class="abs post-name" style="left:579px;top:255px">Blonde Chick</div>
    <p class="abs post-text" style="left:579px;top:283px">Lorem Ipsum is simply dummy text of the printing and typesetting industry. Lorem Ipsum has been</p>
    <div class="abs post-meta" style="left:579px;top:355px"><b>Smith</b>25 mins ago</div>
    <div class="abs share-box" style="left:579px;top:402px">
      <div class="abs stats" style="left:13px;top:10px;font-size:17px"><svg width="34" height="34"><use href="#icon-comment"/></svg>101<svg width="32" height="32"><use href="#icon-like"/></svg>200</div>
      <div class="abs share-btn share-a" style="top:54px"><i></i>SHARE</div>
      <div class="abs count" style="top:54px">56</div>
      <div class="abs like-btn" style="top:54px"><i style="background:var(--sky)"></i>Like</div>
      <div class="abs share-btn share-b" style="top:92px"><i></i>SHARE</div>
      <div class="abs count" style="top:92px">82</div>
      <div class="abs like-btn" style="top:92px"><i style="background:var(--navy)"></i>Like</div>
    </div>
  </article>

  <div class="abs post-rule" style="top:551px"></div>

  <article>
    <h2 class="abs post-heading" style="left:244px;top:560px">Lorem Ipsum is simply dummy</h2>
    <div class="abs post-frame" style="left:245px;top:608px"><div class="abs post-image t-chick" role="img" aria-label="Photo of a yellow chick beside a grey kitten"></div></div>
    <div class="abs post-name" style="left:579px;top:610px">Blonde Chick</div>
    <p class="abs post-text" style="left:579px;top:638px">Lorem Ipsum is simply dummy text of the printing and typesetting industry. Lorem Ipsum has been</p>
    <div class="abs post-meta" style="left:579px;top:710px"><b>Smith</b>25 mins ago</div>
    <div class="abs share-box" style="left:579px;top:757px">
      <div class="abs stats" style="left:13px;top:10px;font-size:17px"><svg width="34" height="34"><use href="#icon-comment"/></svg>101<svg width="32" height="32"><use href="#icon-like"/></svg>200</div>
      <div class="abs share-btn share-a" style="top:54px"><i></i>SHARE</div>
      <div class="abs count" style="top:54px">56</div>
      <div class="abs like-btn" style="top:54px"><i style="background:var(--sky)"></i>Like</div>
      <div class="abs share-btn share-b" style="top:92px"><i></i>SHARE</div>
      <div class="abs count" style="top:92px">82</div>
      <div class="abs like-btn" style="top:92px"><i style="background:var(--navy)"></i>Like</div>
    </div>
  </article>

  <aside class="abs panel" style="left:833px;top:204px;width:349px;height:690px">
    <div class="panel-title">Populer images</div>

    <div class="abs thumb t-elephant" style="left:20px;top:69px;width:168px;height:131px" role="img" aria-label="Photo of an elephant sitting on a toilet"></div>
    <div class="abs item-title" style="left:200px;top:73px">Lorem Ipsum</div>
    <div class="abs stats" style="left:200px;top:107px"><svg width="26" height="26"><use href="#icon-comment"/></svg>101<svg width="26" height="26"><use href="#icon-like"/></svg>200</div>
    <div class="abs divider" style="left:0;top:213px;width:349px"></div>

    <div class="abs thumb t-cart" style="left:20px;top:228px;width:168px;height:131px" role="img" aria-label="Photo of a bicycle piled high with boxes"></div>
    <div class="abs item-title" style="left:200px;top:232px">Lorem Ipsum</div>
    <div class="abs stats" style="left:200px;top:266px"><svg width="26" height="26"><use href="#icon-comment"/></svg>101<svg width="26" height="26"><use href="#icon-like"/></svg>200</div>
    <div class="abs divider" style="left:0;top:372px;width:349px"></div>

    <div class="abs thumb t-kitten" style="left:20px;top:387px;width:168px;height:131px" role="img" aria-label="Photo of a kitten standing with raised paws"></div>
    <div class="abs item-title" style="left:200px;top:391px">Lorem Ipsum</div>
    <div class="abs stats" style="left:200px;top:425px"><svg width="26" height="26"><use href="#icon-comment"/></svg>101<svg width="26" height="26"><use href="#icon-like"/></svg>200</div>
    <div class="abs divider" style="left:0;top:531px;width:349px"></div>

    <div class="abs thumb t-hamster" style="left:20px;top:546px;width:168px;height:131px" role="img" aria-label="Photo of a hamster on a computer mouse"></div>
    <div class="abs item-title" style="left:200px;top:550px">Lorem Ipsum</div>
    <div class="abs stats" style="left:200px;top:584px"><svg width="26" height="26"><use href="#icon-comment"/></svg>101<svg width="26" height="26"><use href="#icon-like"/></svg>200</div>
  </aside>
</main>

<footer class="abs footer">wiz4giggle © 2012&nbsp; All Rights Reserved</footer>

</div>
</body>
</html>
```